Golden Anchor Spin Method Needs a Website

I require a Wordpress website so that I can do simple edits myself. I want it to be a fairly simple design as the videos and the text will speak for themselves.
The concept is simple, we have developed a revolutionary roulette system that proves the game is NOT random. This breakthrough is absolutely massive. We are offering a 12-part training course to take a beginner to a professional at their own pace through watching videos made by our roulette genius.
Roulette and casinos have a glitzy feel about them and this should be reflected in the style of the site. The roulette wheel, table and chips are very evocative and pictures of these would be good.
There is a home page and 5 other pages containing sub-pages. These should be interlinked and it must be easy to get back to the home page from anywhere on the site.
Monflo links should appear at the bottom of each page.
I really need the site in a hurry as we were let down badly by the last developer we hired who went on holiday and left us in the lurch.

Target Market(s)

Gamblers, betting community, opportunity seekers

Coding

Coded - Design and coding required

Number of Pages Required

1 page

Font styles to use
Sans Serif

Requirements
Must have
• At least two videos on the Home page.
• Monflo details on every page and tab.
• A box for name and email address for interested parties to leave their details.

```html
<!DOCTYPE html>
<html lang="en">
<head>
<meta charset="utf-8">
<title>Golden Anchor Spin Method</title>
<link href="https://fonts.googleapis.com/css2?family=Montserrat:wght@400;600;700&family=Open+Sans:wght@400;600&display=swap" rel="stylesheet">
<style>
:root{
  --sidebar:#101c38;
  --sidebar-dark:#0a1122;
  --nav-link:#3f6a93;
  --nav-line:#1f2e50;
  --white:#ffffff;
  --body-text:#d9dde6;
  --panel:#1b2a57;
  --field:#0c1429;
  --bar:#222222;
  --gold-light:#ffe49a;
  --gold:#f3b23c;
  --black:#000000;
}
*{box-sizing:border-box;margin:0;padding:0}
html,body{width:958px;height:1200px;overflow:hidden;background:var(--black)}
body{position:relative;font-family:"Open Sans",Arial,sans-serif;color:var(--body-text)}
.stage{position:absolute;inset:0;background:var(--black)}
.hero-backdrop{position:absolute;left:160px;top:0;width:798px;height:680px;
  background:
    radial-gradient(ellipse 320px 240px at 470px 150px,rgba(60,80,160,.55),transparent 70%),
    radial-gradient(ellipse 260px 200px at 700px 300px,rgba(110,40,120,.45),transparent 70%),
    radial-gradient(ellipse 200px 180px at 120px 330px,rgba(140,50,30,.35),transparent 70%),
    linear-gradient(180deg,#1a2450 0%,#121a3a 45%,#000 100%)}
.sidebar{position:absolute;left:0;top:0;width:160px;height:1200px;
  background:linear-gradient(180deg,#111d3b 0%,#0f1a35 60%,#101c38 100%)}
.nav{list-style:none;position:absolute;left:4px;top:0;width:151px}
.nav-item{position:absolute;left:0;width:151px;border-bottom:1px solid var(--nav-line);
  font-family:"Montserrat",sans-serif;font-size:10.2px;font-weight:600;color:var(--nav-link);
  padding-left:8px;letter-spacing:.2px}
.nav-item.active{color:var(--white)}
.nav-item .caret{position:absolute;right:6px;top:1px;width:7px;height:7px}
.subnav{position:absolute;left:4px;top:99px;width:151px;height:133px;background:var(--sidebar-dark);list-style:none}
.subnav li{position:absolute;left:9px;font-size:7.4px;color:#9aa6bd}
.subnav li.current{color:var(--white)}
.subnav li::before{content:"•";margin-right:4px;color:#6f7c96}
.subnav li.current::before{content:"›";color:var(--white)}
.copyright{position:absolute;left:15px;top:1138px;font-size:7.4px;line-height:14px;color:#9aa6bd}
.title{position:absolute;left:181px;width:587px;top:20px;text-align:center;
  font-family:"Montserrat",sans-serif;font-weight:600;font-size:32px;letter-spacing:.5px;
  background:linear-gradient(180deg,var(--gold-light) 0%,var(--gold) 100%);
  -webkit-background-clip:text;background-clip:text;color:transparent}
.copy{position:absolute;left:181px;width:587px;font-size:7.3px;line-height:15.2px;color:var(--body-text)}
.video{position:absolute;left:181px;width:587px;height:191px;border:3px solid #2c2c2c;
  background:radial-gradient(ellipse at 60% 40%,#5a5a5a,#1b1b1b 75%)}
.video.second{background:radial-gradient(ellipse at 40% 35%,#6a6a6a,#222 75%)}
.video-label{position:absolute;left:0;right:0;top:67px;text-align:center;
  font-family:"Montserrat",sans-serif;font-weight:600;font-size:11.5px;color:var(--white)}
.video svg{position:absolute;left:270px;top:89px}
.newsletter-bar{position:absolute;left:181px;top:1045px;width:587px;height:51px;background:var(--bar)}
.newsletter-bar .label{position:absolute;left:53px;top:19px;font-family:"Montserrat",sans-serif;font-weight:600;font-size:10.2px;color:var(--white)}
.field{position:absolute;background:var(--field);border:1px solid #11182b;font-size:7.4px;color:#6c7890;padding-left:9px;display:flex;align-items:center}
.newsletter-bar .field{background:#111;border-color:#1a1a1a}
.button{position:absolute;background:linear-gradient(180deg,#f4f4f4,#bdbdbd);color:#222;font-size:7.6px;display:flex;align-items:center;justify-content:center}
.payments{position:absolute;left:250px;top:1138px;width:460px;height:40px;display:flex;align-items:center;justify-content:space-between}
.pay{display:flex;align-items:center;gap:6px;font-family:"Montserrat",sans-serif;font-weight:700;font-size:17px;color:#c9d3e6}
.pay .dot{width:10px;height:10px;border-radius:50%;background:#3a5aa0}
.card{position:absolute;left:790px;width:159px;background:rgba(27,42,87,.92)}
.card h3{position:absolute;left:12px;font-family:"Montserrat",sans-serif;font-weight:600;font-size:10.2px;color:var(--white)}
.contact-line{position:absolute;left:12px;font-size:7.2px;color:#9aa6bd;display:flex;align-items:center;gap:6px}
.contact-line svg{width:7px;height:7px}
</style>
</head>
<body>
<div class="stage">
  <div class="hero-backdrop" role="img" aria-label="Blurred casino photograph of a roulette wheel and chips in blue and purple light"></div>

  <aside class="sidebar">
    <ul class="nav">
      <li class="nav-item active" style="top:24px;height:30px">INTRODUCTION</li>
      <li class="nav-item" style="top:69px;height:30px">TRAINING<svg class="caret" viewBox="0 0 8 8"><path d="M1 2.5l3 3 3-3" fill="none" stroke="#3f6a93" stroke-width="1.2"/></svg></li>
      <li class="nav-item" style="top:248px;height:29px">CASINOS<svg class="caret" viewBox="0 0 8 8"><path d="M1 2.5l3 3 3-3" fill="none" stroke="#3f6a93" stroke-width="1.2"/></svg></li>
      <li class="nav-item" style="top:293px;height:29px">COACHING<svg class="caret" viewBox="0 0 8 8"><path d="M1 2.5l3 3 3-3" fill="none" stroke="#3f6a93" stroke-width="1.2"/></svg></li>
      <li class="nav-item" style="top:338px;height:29px">OVERSEAS TRIP<svg class="caret" viewBox="0 0 8 8"><path d="M1 2.5l3 3 3-3" fill="none" stroke="#3f6a93" stroke-width="1.2"/></svg></li>
      <li class="nav-item" style="top:383px;height:29px">FAQ</li>
    </ul>
    <ul class="subnav">
      <li class="current" style="top:13px">Course Description</li>
      <li style="top:45px">Monthly Membership</li>
      <li style="top:77px">The Complete System</li>
      <li style="top:109px">Intellectual Property Rights</li>
    </ul>
    <p class="copyright">Copyright © 2016<br>Golden Anchor Spin Method<br>All rights reserved.</p>
  </aside>

  <h1 class="title">GOLDEN ANCHOR SPIN METHOD</h1>

  <p class="copy" style="top:83px">Introducing the incredible Golden Anchor roulette system. Four years in the making by a roulette genius who has observed hundreds of thousands of spins to create a truly groundbreaking system. Every aspect of the game has been broken down, analysed and rebuilt with a solution. This system questions whether the game of roulette is truly random……and the answer is a resounding NO !!</p>
  <p class="copy" style="top:144px">The key to success is long term profits but to achieve that you need to look beyond complexity and concentrate on simplicity. The system reverses general logic and considers the number of losses rather than the number of wins. This led to the discovery of the counting system, a perfect, carefully balanced approach to progression that protects your bankroll at all times. This alone would be the perfect complement for any roulette system but when combined with the rules of Golden Anchor, it's dynamite.</p>

  <div class="video" style="top:220px" role="img" aria-label="Video poster: close-up photograph of a roulette wheel">
    <div class="video-label">WATCH THIS VIDEO AND PREPARE TO BE AMAZED</div>
    <svg width="46" height="46" viewBox="0 0 46 46"><circle cx="23" cy="23" r="20.5" fill="none" stroke="#fff" stroke-width="3"/><path d="M18 13.5v19l15-9.5z" fill="#fff"/></svg>
  </div>

  <p class="copy" style="top:428px">The second major breakthrough was the discovery of the families. These are groups of numbers that appear regularly within a few spins of each other. For students learning the system, this is their first 'wow' moment. The regularity of hits between numbers in the families is staggering and underpins the whole system.</p>
  <p class="copy" style="top:489px">Finally, the families were analysed further and broken down into pairs. This provided the opportunity to shorten the average playing time of each session to around half an hour. The philosophy of Golden Anchor is to build your stakes slowly and then when everything falls into place, make a big win and walk away.</p>

  <div class="video second" style="top:547px" role="img" aria-label="Video poster: black and white photograph of a roulette wheel">
    <div class="video-label">WATCH THIS VIDEO AND PREPARE TO BE AMAZED</div>
    <svg width="46" height="46" viewBox="0 0 46 46"><circle cx="23" cy="23" r="20.5" fill="none" stroke="#fff" stroke-width="3"/><path d="M18 13.5v19l15-9.5z" fill="#fff"/></svg>
  </div>

  <p class="copy" style="top:753px">We are offering a unique opportunity to learn the Golden Anchor system through a series of videos made by our very own roulette genius. You will learn every aspect of this amazing system at your own pace, only moving on to the next stage when you have totally mastered the previous step. We encourage our students to practise their skills in play mode and when they are completely confident and winning every session, play with real money. This allows them to build their bankroll and pay for each video as they go along.</p>
  <p class="copy" style="top:830px">Our course has been designed to make each step easy to learn and understand. Each video leads into the next and builds a new layer of understanding on top of the last. Committing the information to memory is very easy using this method and our students become experts at analysing everything unfolding before them in a roulette session.</p>
  <p class="copy" style="top:891px">Some of our students become professional players, enjoying the thrills of playing in bricks and mortar casinos around the world. Others are happy to play part-time from home and build a second income. The fact is that once you have the skills to be successful at roulette, the options really are endless. We are only successful if our students achieve their goals. We provide individual coaching sessions if anyone needs extra tuition and will always endeavor to answer questions quickly. Upon completion of the course, we will also play for our students so that they can watch and learn.</p>
  <p class="copy" style="top:968px">The highlight of the year is undoubtedly the Golden Anchor Las Vegas trip. A chance to meet the team and fellow students who have learnt the system. The emphasis is very much on the 'business' of making money with a little 'pleasure' thrown in after a day of play at the tables.</p>
  <p class="copy" style="top:1014px">We invite you to have a look around the site and ask us any questions. It will be our pleasure to enroll you as the next student of Golden Anchor.</p>

  <form class="newsletter-bar">
    <span class="label">NEWSLETTER SIGNUP</span>
    <div class="field" style="left:181px;top:14px;width:134px;height:23px">Name</div>
    <div class="field" style="left:328px;top:14px;width:134px;height:23px">Email</div>
    <div class="button" style="left:474px;top:14px;width:59px;height:23px">Subscribe</div>
  </form>

  <div class="payments">
    <span class="pay"><span class="dot"></span>Cardora</span>
    <span class="pay">Vantix</span>
    <span class="pay">Amberline</span>
    <span class="pay">Monflo</span>
  </div>

  <section class="card" style="top:10px;height:117px">
    <h3 style="top:15px">CONTACT INFO</h3>
    <div class="contact-line" style="top:44px"><svg viewBox="0 0 8 8"><rect x="0.5" y="1.5" width="7" height="5" fill="none" stroke="#9aa6bd"/><path d="M.5 1.5l3.5 3 3.5-3" fill="none" stroke="#9aa6bd"/></svg>support@goldenanchorspin.com</div>
    <div class="contact-line" style="top:64px"><svg viewBox="0 0 8 8"><circle cx="4" cy="4" r="3.3" fill="none" stroke="#9aa6bd"/></svg>Martin Hale</div>
    <div class="contact-line" style="top:84px"><svg viewBox="0 0 8 8"><rect x="2" y="0.5" width="4" height="7" rx="0.6" fill="none" stroke="#9aa6bd"/></svg>Text: 07900 000123</div>
  </section>

  <section class="card" style="top:121px;height:133px">
    <h3 style="top:14px">NEWSLETTER SIGNUP</h3>
    <div class="field" style="left:12px;top:35px;width:135px;height:23px">Name</div>
    <div class="field" style="left:12px;top:67px;width:135px;height:23px">Email</div>
    <div class="button" style="left:12px;top:99px;width:59px;height:23px">Subscribe</div>
  </section>
</div>
</body>
</html>
```